Harborline Energy - needs a business card

Harborline Energy is a U.S. based diesel sourcing and distribution company that supports American oil & gas fields through providing quality product and consistent services.

Target Market(s)

Oil and Gas

Contact Information for Business Card

The background of the card must be white to ensure the logo pops.

Font styles to use
Serif
Sans Serif

Colors

Designer to choose colors to be used in the design.

Requirements
Must have
• Front of Card: Tag line: Harborline Energy, Powering America's Oil & Gas fields.
• Not sure if you guys do this part but just in case...
• Dale Menschow
• Owner/CEO
• C:555.318.4076
• E:Dmenschow@harborlineenergy.example
• W:Harborlineenergy.example
• Locations: Servicing the Powder River, DJ basin and Bakken formations.
• Back of Card: " Frac fueling is what we do. We understand how important diesel fuel is to your operation, which is why our main service line is Frac fueling. We assure our supply and stand by our service"

```html
<!DOCTYPE html>
<html lang="en">
<head>
<meta charset="utf-8">
<title>Harborline Energy – Business Card</title>
<link href="https://fonts.googleapis.com/css2?family=Lato:ital,wght@0,400;0,700;0,900;1,400&display=swap" rel="stylesheet">
<style>
  :root {
    --navy: #1a2a5e;
    --red: #b5121b;
    --deep-red: #8e0f22;
    --ink: #3a3a3a;
    --muted: #6b6b6b;
    --rule: #c9c9c9;
    --paper: #ffffff;
    --stage: #e4e5e8;
  }
  * { box-sizing: border-box; margin: 0; padding: 0; }
  html, body { width: 1200px; height: 896px; overflow: hidden; }
  body {
    background: var(--stage);
    font-family: "Lato", Arial, sans-serif;
    display: flex;
    flex-direction: column;
    align-items: center;
    justify-content: center;
    gap: 28px;
  }
  .card {
    position: relative;
    width: 700px;
    height: 400px;
    overflow: hidden;
    box-shadow: 0 6px 18px rgba(0,0,0,.18);
  }

  /* Front */
  .card--front { background: var(--paper); }
  .brand {
    position: absolute;
    top: 70px;
    right: 48px;
    width: 380px;
    text-align: center;
  }
  .brand__mark {
    display: inline-flex;
    align-items: center;
    gap: 14px;
  }
  .brand__dot {
    width: 48px; height: 48px;
    border-radius: 50%;
    background: var(--navy);
  }
  .brand__name {
    font-weight: 900;
    font-size: 38px;
    letter-spacing: 1px;
    color: var(--navy);
    text-transform: uppercase;
  }
  .brand__tagline {
    margin-top: 14px;
    font-size: 11.5px;
    font-weight: 700;
    color: var(--ink);
    text-transform: uppercase;
    letter-spacing: .2px;
  }
  .contact {
    position: absolute;
    left: 40px;
    top: 150px;
    width: 300px;
  }
  .contact__name {
    font-size: 26px;
    font-weight: 700;
    text-transform: uppercase;
    line-height: 1;
  }
  .contact__first { color: var(--navy); }
  .contact__last { color: var(--red); }
  .contact__role {
    font-size: 17px;
    color: var(--muted);
    margin: 4px 0 12px;
  }
  .contact__list { list-style: none; }
  .contact__item {
    display: flex;
    align-items: center;
    gap: 9px;
    font-size: 14.5px;
    color: var(--ink);
    margin-bottom: 5px;
  }
  .contact__item svg { width: 14px; height: 14px; flex: none; fill: var(--navy); }
  .contact__rule {
    width: 330px;
    height: 1px;
    background: var(--rule);
    margin-top: 14px;
  }
  .locations {
    position: absolute;
    right: 52px;
    bottom: 62px;
    width: 250px;
    padding-top: 12px;
    border-top: 1px solid var(--rule);
    font-size: 16px;
    line-height: 1.3;
    color: var(--ink);
  }
  .locations__label { color: var(--red); }
  .band {
    position: absolute;
    left: 0; bottom: 0;
    width: 100%;
    height: 14px;
  }

  /* Back */
  .card--back {
    background: linear-gradient(120deg, var(--navy) 0%, #3a1f52 40%, var(--deep-red) 75%, var(--red) 100%);
    color: #fff;
    display: flex;
    flex-direction: column;
    justify-content: center;
    padding: 0 60px;
    text-align: center;
  }
  .pitch {
    font-size: 17px;
    line-height: 1.55;
    text-transform: uppercase;
    letter-spacing: .3px;
  }
  .pitch__rule {
    width: 420px;
    height: 1px;
    background: rgba(255,255,255,.6);
    margin: 26px auto 18px;
  }
  .pitch__tagline {
    font-size: 15px;
    font-weight: 700;
    text-transform: uppercase;
  }
</style>
</head>
<body>

  <section class="card card--front" aria-label="Business card front">
    <div class="brand">
      <div class="brand__mark">
        <span class="brand__dot"></span>
        <span class="brand__name">Harborline Energy</span>
      </div>
      <p class="brand__tagline">Harborline Energy, Powering America's Oil &amp; Gas fields</p>
    </div>

    <div class="contact">
      <h1 class="contact__name"><span class="contact__first">Dale</span> <span class="contact__last">Menschow</span></h1>
      <p class="contact__role">Owner/CEO</p>
      <ul class="contact__list">
        <li class="contact__item">
          <svg viewBox="0 0 16 16" aria-hidden="true"><path d="M3 1h3l1.5 4-2 1.2a9 9 0 0 0 4.3 4.3L11 8.5l4 1.5v3a2 2 0 0 1-2 2A13 13 0 0 1 1 3a2 2 0 0 1 2-2z"/></svg>
          555.318.4076
        </li>
        <li class="contact__item">
          <svg viewBox="0 0 16 16" aria-hidden="true"><path d="M1 3h14v10H1z M2 4l6 5 6-5" fill="none" stroke="#1a2a5e" stroke-width="1.6"/></svg>
          Dmenschow@harborlineenergy.example
        </li>
        <li class="contact__item">
          <svg viewBox="0 0 16 16" aria-hidden="true"><circle cx="8" cy="8" r="7"/></svg>
          www.Harborlineenergy.example
        </li>
      </ul>
      <div class="contact__rule"></div>
    </div>

    <p class="locations"><span class="locations__label">Locations:</span> Servicing the Powder River DJ basin and Bakken formations</p>

    <svg class="band" viewBox="0 0 700 14" preserveAspectRatio="none" aria-hidden="true">
      <rect width="700" height="14" fill="var(--red)"/>
      <polygon points="0,0 270,0 284,14 0,14" fill="var(--navy)"/>
    </svg>
  </section>

  <section class="card card--back" aria-label="Business card back">
    <p class="pitch">Frac fueling is what we do. We understand how important diesel fuel is to your operation which is why our main service line is frac fueling. We assure our supply and stand by our service</p>
    <div class="pitch__rule"></div>
    <p class="pitch__tagline">Harborline Energy, Powering America's Oil &amp; Gas fields.</p>
  </section>

</body>
</html>
```